Brook Outreach eCommerce (a-la-carte) Modern Edgy (Be Creative - Follow Brief)

//BROOK OUTREACH//
A-La-Carte style eCommerce site designed with pick and pay options. Full credit card payment gateway. SendWise offered, Google Pay, Apple Pay. (Open to suggestions: Wordpress, BigCommerce, Squarespace)

Designed to fit look and feel of logo. Warm, Inviting, Simple and Modern.

Pages (standard 5):
1. Main Page: Sample Cases/Photos, Hot Packages
2. About: Company statement, Staff bios, Our goals
3. Services: Place to list options, service offerings, prices of packages (ability to check out, pay, etc)
4. Portfolio: Place to showcase our work, testimonials, ratings
5. Contact: Contact form, Links to other platforms (Pingo, Wavelet, Guildhall)

Links to Social Media, include ability to share throughout whole page.

***(See attached Logo - use for look and feel but feel free to be creative, only a suggestion)***

Target Market(s)

Business, Influencers, Brands

Industry/Entity Type

Branding & Marketing

Coding

Coded - Design and coding required

Number of Pages Required

5+ page

Colors
0054AA
0677BA
7BADD7
CADEEF
E8F1F8

Requirements
Must have
• Must be clean, easy to navigate, modern look and feel but warm and inviting
Nice to have
• Front Page - Main "HOT" offerings // About Page // Contact Page (Form - Links to Pingo, Wavelet, Guildhall) // Services // Portfolio page -- Social Media Links
Should not have
• clutter.

```html
<!DOCTYPE html>
<html lang="en">
<head>
<meta charset="utf-8">
<title>Brook Outreach — eCommerce Marketing Agency</title>
<link href="https://fonts.googleapis.com/css2?family=Poppins:wght@400;500;600;700;800&family=Great+Vibes&display=swap" rel="stylesheet">
<style>
:root{
  --teal:#2fb0cb;
  --teal-light:#7fd3e2;
  --teal-dark:#2b8ea6;
  --navy:#1c2240;
  --ink:#222633;
  --muted:#4a4f5c;
  --pale:#eef6fb;
  --dark:#1d1e22;
  --bar:#141416;
  --pink:#f0457a;
  --violet:#8c7fe0;
  --white:#ffffff;
}
*{margin:0;padding:0;box-sizing:border-box}
html,body{width:1200px;height:5348px;overflow:hidden}
body{font-family:"Poppins",sans-serif;color:var(--ink);background:var(--white);position:relative}
.abs{position:absolute}
section,header,footer,nav{position:absolute;left:0;width:1200px}
.script{font-family:"Great Vibes",cursive;color:var(--teal-dark);font-weight:400;opacity:.85}
.heading{font-weight:800;color:var(--ink);letter-spacing:.5px;position:relative}
.pill{display:inline-flex;align-items:center;justify-content:center;gap:8px;border-radius:30px;font-weight:600;font-size:15px;color:var(--white)}
.ring-svg{position:absolute;left:0;top:0;pointer-events:none}

/* top bar + nav */
.topbar{top:0;height:48px;background:var(--bar)}
.chips{display:flex;gap:10px}
.chips span{font-size:11px;color:#ddd;display:flex;align-items:center;gap:5px}
.chips span::before{content:"";width:8px;height:8px;border-radius:50%;background:#ddd}
.topbar .chips{position:absolute;left:86px;top:16px}
.nav{top:48px;height:91px;background:#1f2024}
.brand{font-size:20px;font-weight:600;color:var(--white);top:32px;left:86px;display:flex;align-items:center;gap:10px}
.brand i{width:14px;height:14px;border-radius:50%;background:var(--teal);display:block}
.menu{right:86px;top:34px;display:flex;gap:48px;font-size:15px;color:#e6e6e6;list-style:none}
.menu li:first-child{color:var(--teal)}

/* hero */
.hero{top:139px;height:538px;overflow:hidden}
.hero .photo{left:0;top:0;width:1200px;height:538px;
  background:
   radial-gradient(ellipse 260px 300px at 790px 300px,rgba(40,48,70,.55),rgba(40,48,70,0) 70%),
   radial-gradient(ellipse 220px 280px at 990px 260px,rgba(226,206,178,.7),rgba(226,206,178,0) 70%),
   linear-gradient(100deg,#174e5c 0%,#2d7888 26%,#8aa9b4 46%,#cfd3d2 64%,#e9e4dc 100%)}
.hero h1{left:105px;top:170px;font-size:48px;line-height:60px;font-weight:600;color:var(--white)}
.hero h1 span{color:var(--teal-light)}
.btn-ghost{left:105px;top:306px;width:176px;height:50px;border:2px solid var(--white);font-size:14px}

/* about */
.about{top:677px;height:652px}
.about .frame{left:130px;top:80px;width:440px;height:440px}
.about .photo{position:absolute;left:30px;top:30px;width:380px;height:380px;border-radius:50%;
  background:radial-gradient(circle at 50% 65%,#c9ccd2 0,#dfe3e8 45%,#f2f4f6 80%)}
.about .script{left:610px;top:92px;font-size:88px}
.about .heading{left:610px;top:200px;font-size:60px}
.about p{left:612px;top:290px;width:500px;font-size:15px;line-height:28px;color:var(--muted)}
.btn-teal{background:var(--teal-dark)}
.about .btn-teal{left:612px;top:436px;width:186px;height:54px}

/* services */
.services{top:1329px;height:656px;background:var(--pale)}
.title-wrap{left:0;width:1200px;text-align:center}
.title-wrap .script{font-size:96px;line-height:1;display:block;height:60px}
.title-wrap .heading{font-size:60px;display:block}
.services .title-wrap{top:70px}
.svc{width:240px;text-align:center}
.svc .frame{position:relative;width:240px;height:240px}
.svc .photo{position:absolute;left:14px;top:14px;width:212px;height:212px;border-radius:50%}
.svc h3{margin-top:14px;font-size:19px;line-height:28px;font-weight:600}

/* packages */
.packages{top:1985px;height:886px}
.packages .title-wrap{top:90px}
.card{top:267px;width:322px;height:516px;background:var(--white);border-radius:16px;box-shadow:0 4px 22px rgba(60,80,120,.16);text-align:center}
.card h3{margin-top:20px;font-size:24px;font-weight:600}
.card hr{border:0;height:2px;margin:14px 24px 0}
.card .price{margin-top:18px;font-size:42px;font-weight:600;color:var(--navy);line-height:48px}
.card .price small{font-size:20px}
.card .per{font-size:17px;color:var(--muted)}
.card ul{list-style:none;text-align:left;margin:18px 24px 0 26px;font-size:14px;line-height:21px;color:var(--muted)}
.card li{display:flex;gap:10px;margin-bottom:17px}
.card li svg{flex:none;margin-top:3px}
.card .pill{position:absolute;left:45px;bottom:30px;width:240px;height:50px;font-size:15px}
.free h3{color:var(--pink)}.free hr{background:var(--pink)}.free .pill{background:linear-gradient(90deg,#f2588e,#f0457a)}
.basic h3{color:var(--violet)}.basic hr{background:var(--violet)}.basic .pill{background:linear-gradient(90deg,#8c7fe0,#a08de8)}
.premium h3{color:var(--teal)}.premium hr{background:var(--teal)}.premium .pill{background:linear-gradient(90deg,#49a7c2,#50d4e0)}

/* portfolio */
.portfolio{top:2871px;height:706px;background:var(--pale)}
.portfolio .title-wrap{top:60px}
.work{width:360px;text-align:center}
.work .frame{position:relative;width:260px;height:260px;margin:0 auto}
.work .photo{position:absolute;left:10px;top:20px;width:236px;height:236px;border-radius:50%}
.work h3{margin-top:20px;font-size:19px;font-weight:600}
.work p{margin-top:6px;font-size:15px;line-height:28px;color:var(--muted)}

/* testimonials */
.testimonials{top:3577px;height:720px}
.testimonials .title-wrap{top:45px}
.quote{border-radius:50%;background:var(--white);box-shadow:0 6px 18px rgba(0,0,0,.14);text-align:center;display:flex;flex-direction:column;align-items:center;justify-content:center}
.quote .mark{font-size:70px;line-height:50px;color:var(--teal);font-weight:700;height:44px}
.quote p{font-size:13px;line-height:24px;color:var(--muted);margin-top:12px}
.quote b{margin-top:10px;font-size:16px;color:var(--navy)}
.quote em{font-size:12px;color:var(--muted)}
.quote.main{background:var(--teal);box-shadow:0 0 0 8px var(--white),0 0 0 14px var(--teal)}
.quote.main .mark,.quote.main p,.quote.main b,.quote.main em{color:var(--white)}
.quote.main p{font-size:15px;line-height:26px}

/* contact */
.contact{top:4297px;height:623px;overflow:hidden}
.contact .script{left:78px;top:100px;font-size:80px}
.contact .heading{left:85px;top:165px;font-size:56px}
.field{height:44px;border:1px solid #d7dbe2;border-radius:4px;font-size:13px;color:#8a8f99;padding:12px 14px}
.contact .btn-teal{left:85px;top:525px;width:218px;height:48px}
.contact .figure{left:700px;top:90px;width:470px;height:533px;border-radius:230px 230px 0 0;
  background:
   radial-gradient(ellipse 110px 120px at 260px 150px,#d9b89c 0,rgba(217,184,156,0) 75%),
   linear-gradient(180deg,rgba(255,255,255,0) 0,rgba(255,255,255,0) 30%,#aeb3b8 45%,#8d939b 100%)}

/* footer */
.footer{top:4920px;height:428px;background:var(--dark);color:#dcdcdc}
.footer h4{font-size:16px;font-weight:600;color:var(--white)}
.footer p,.footer li{font-size:14px;line-height:28px}
.footer ul{list-style:none}
.footer li::before{content:"›";color:var(--teal);margin-right:12px}
.contact-row{display:flex;gap:14px;font-size:14px;line-height:28px}
.contact-row svg{flex:none;margin-top:7px}
.payments{left:885px;top:300px;display:flex;gap:14px}
.payments span{width:48px;height:30px;background:var(--white);border-radius:4px;font-size:9px;color:var(--navy);font-weight:600;display:flex;align-items:center;justify-content:center}
.footer .rule{left:0;top:350px;width:1200px;height:1px;background:#333}
.copy{left:0;top:378px;width:1200px;text-align:center;font-size:14px}
.copy span{color:var(--teal)}
</style>
</head>
<body>

<header class="topbar">
  <div class="chips"><span>Pingo</span><span>Wavelet</span><span>Guildhall</span></div>
  <svg class="abs" style="right:86px;top:14px" width="60" height="20" viewBox="0 0 60 20" aria-label="Account and cart">
    <circle cx="10" cy="7" r="4" fill="#fff"/><path d="M3 18c0-4 3-6 7-6s7 2 7 6z" fill="#fff"/>
    <path d="M36 6h3l3 10h12l3-8H41" fill="none" stroke="#fff" stroke-width="2"/>
    <circle cx="56" cy="4" r="4" fill="#2fb0cb"/>
  </svg>
</header>

<nav class="nav">
  <div class="abs brand"><i></i>Brook Outreach</div>
  <ul class="abs menu"><li>HOME</li><li>ABOUT</li><li>SERVICES</li><li>PORTFOLIO</li><li>CONTACT</li></ul>
</nav>

<section class="hero">
  <div class="abs photo" role="img" aria-label="Photo of two colleagues working together at a laptop in a bright office"></div>
  <svg class="abs" style="left:60px;top:30px" width="520" height="480" viewBox="0 0 520 480" aria-hidden="true">
    <ellipse cx="250" cy="240" rx="210" ry="200" fill="none" stroke="#5fd0e3" stroke-width="14" stroke-dasharray="520 800" stroke-dashoffset="-120" stroke-linecap="round" opacity=".85"/>
    <ellipse cx="250" cy="240" rx="225" ry="215" fill="none" stroke="#9fe4ef" stroke-width="4" stroke-dasharray="420 900" stroke-dashoffset="-160" stroke-linecap="round" opacity=".7"/>
  </svg>
  <h1 class="abs">eCommerce<br><span>Marketing</span> Agency</h1>
  <div class="abs pill btn-ghost">Learn More →</div>
</section>

<section class="about">
  <div class="abs frame">
    <div class="photo" role="img" aria-label="Photo of two team members smiling at a laptop"></div>
    <svg class="ring-svg" width="440" height="440" viewBox="0 0 440 440" aria-hidden="true">
      <circle cx="220" cy="220" r="200" fill="none" stroke="#2fb0cb" stroke-width="16" stroke-dasharray="700 560" stroke-dashoffset="-60" stroke-linecap="round" transform="rotate(20 220 220)"/>
      <circle cx="220" cy="220" r="212" fill="none" stroke="#7fd3e2" stroke-width="6" stroke-dasharray="500 840" stroke-dashoffset="-640" stroke-linecap="round"/>
    </svg>
  </div>
  <div class="abs script">About</div>
  <h2 class="abs heading">Brook Outreach</h2>
  <p class="abs">Lorem ipsum dolor sit amet, consectetur adipiscing elit, sed do eiusmod tempor incididunt ut labore et dolore magna aliqua. Quis ipsum suspendisse ultrices gravida. Risus cmodo viverra maecenas accumsan lacus vel facilisis.</p>
  <div class="abs pill btn-teal">Learn More →</div>
</section>

<section class="services">
  <div class="abs title-wrap"><span class="script">Services</span><span class="heading">Service Offerings</span></div>

  <div class="abs svc" style="left:76px;top:253px">
    <div class="frame">
      <div class="photo" style="background:radial-gradient(circle at 40% 45%,#7a4a6a 0,#3b2c3e 55%,#2a2230 100%)" role="img" aria-label="Photo of a woman surrounded by social media icons"></div>
      <svg class="ring-svg" width="240" height="240" viewBox="0 0 240 240" aria-hidden="true"><circle cx="120" cy="120" r="110" fill="none" stroke="#2fb0cb" stroke-width="10" stroke-dasharray="420 300" stroke-linecap="round" transform="rotate(60 120 120)"/><circle cx="120" cy="120" r="117" fill="none" stroke="#7fd3e2" stroke-width="4" stroke-dasharray="200 535" stroke-linecap="round" transform="rotate(200 120 120)"/></svg>
    </div>
    <h3>Socila Media<br>Marketing</h3>
  </div>

  <div class="abs svc" style="left:345px;top:253px">
    <div class="frame">
      <div class="photo" style="background:radial-gradient(circle at 50% 40%,#6a5a8a 0,#3a3550 55%,#221f2c 100%)" role="img" aria-label="Photo of an influencer recording a video"></div>
      <svg class="ring-svg" width="240" height="240" viewBox="0 0 240 240" aria-hidden="true"><circle cx="120" cy="120" r="110" fill="none" stroke="#2fb0cb" stroke-width="10" stroke-dasharray="420 300" stroke-linecap="round" transform="rotate(60 120 120)"/><circle cx="120" cy="120" r="117" fill="none" stroke="#7fd3e2" stroke-width="4" stroke-dasharray="200 535" stroke-linecap="round" transform="rotate(200 120 120)"/></svg>
    </div>
    <h3>Influencer<br>Marketing</h3>
  </div>

  <div class="abs svc" style="left:613px;top:253px">
    <div class="frame">
      <div class="photo" style="background:radial-gradient(circle at 50% 40%,#2d3340 0,#4b5160 50%,#c9cdd3 100%)" role="img" aria-label="Photo of a screen showing a content marketing graphic"></div>
      <svg class="ring-svg" width="240" height="240" viewBox="0 0 240 240" aria-hidden="true"><circle cx="120" cy="120" r="110" fill="none" stroke="#2fb0cb" stroke-width="10" stroke-dasharray="420 300" stroke-linecap="round" transform="rotate(60 120 120)"/><circle cx="120" cy="120" r="117" fill="none" stroke="#7fd3e2" stroke-width="4" stroke-dasharray="200 535" stroke-linecap="round" transform="rotate(200 120 120)"/></svg>
    </div>
    <h3>Content<br>Marketing</h3>
  </div>

  <div class="abs svc" style="left:883px;top:253px">
    <div class="frame">
      <div class="photo" style="background:radial-gradient(circle at 60% 40%,#8a93a3 0,#4d5566 55%,#2c313c 100%)" role="img" aria-label="Photo of hands typing on a keyboard"></div>
      <svg class="ring-svg" width="240" height="240" viewBox="0 0 240 240" aria-hidden="true"><circle cx="120" cy="120" r="110" fill="none" stroke="#2fb0cb" stroke-width="10" stroke-dasharray="420 300" stroke-linecap="round" transform="rotate(60 120 120)"/><circle cx="120" cy="120" r="117" fill="none" stroke="#7fd3e2" stroke-width="4" stroke-dasharray="200 535" stroke-linecap="round" transform="rotate(200 120 120)"/></svg>
    </div>
    <h3>Paid<br>Advertisign</h3>
  </div>
</section>

<section class="packages">
  <div class="abs title-wrap"><span class="script">Hot</span><span class="heading">Packages</span></div>

  <div class="abs card free" style="left:87px">
    <h3>Free</h3><hr>
    <div class="price"><small>$</small>49</div><div class="per">Per Month</div>
    <ul>
      <li><svg width="14" height="12"><path d="M1 6l4 4 8-9" fill="none" stroke="#2e9a3a" stroke-width="2.5"/></svg>Proin est leo, placerat at suscipit id, cursus id dolor.</li>
      <li><svg width="14" height="12"><path d="M1 6l4 4 8-9" fill="none" stroke="#2e9a3a" stroke-width="2.5"/></svg>Praesent id arcu slue, malesuada velit faucibus metus.</li>
      <li><svg width="14" height="12"><path d="M1 6l4 4 8-9" fill="none" stroke="#2e9a3a" stroke-width="2.5"/></svg>Donec dolor lacus, tempor eu enim id, porta sagittis nunc.</li>
      <li><svg width="14" height="12"><path d="M1 6l4 4 8-9" fill="none" stroke="#2e9a3a" stroke-width="2.5"/></svg>Aliquam erat volutpabitur tortor justo,</li>
    </ul>
    <div class="pill">Get This Plan →</div>
  </div>

  <div class="abs card basic" style="left:438px">
    <h3>Basic</h3><hr>
    <div class="price"><small>$</small>189</div><div class="per">Per Month</div>
    <ul>
      <li><svg width="14" height="12"><path d="M1 6l4 4 8-9" fill="none" stroke="#2e9a3a" stroke-width="2.5"/></svg>Proin est leo, placerat at suscipit id, cursus id dolor.</li>
      <li><svg width="14" height="12"><path d="M1 6l4 4 8-9" fill="none" stroke="#2e9a3a" stroke-width="2.5"/></svg>Praesent id arcu slue, malesuada velit faucibus metus.</li>
      <li><svg width="14" height="12"><path d="M1 6l4 4 8-9" fill="none" stroke="#2e9a3a" stroke-width="2.5"/></svg>Donec dolor lacus, tempor eu enim id, porta sagittis nunc.</li>
      <li><svg width="14" height="12"><path d="M1 6l4 4 8-9" fill="none" stroke="#2e9a3a" stroke-width="2.5"/></svg>Aliquam erat volutpabitur tortor justo,</li>
    </ul>
    <div class="pill">Get This Plan →</div>
  </div>

  <div class="abs card premium" style="left:787px">
    <h3>Premium</h3><hr>
    <div class="price"><small>$</small>299</div><div class="per">Per Month</div>
    <ul>
      <li><svg width="14" height="12"><path d="M1 6l4 4 8-9" fill="none" stroke="#2e9a3a" stroke-width="2.5"/></svg>Proin est leo, placerat at suscipit id, cursus id dolor.</li>
      <li><svg width="14" height="12"><path d="M1 6l4 4 8-9" fill="none" stroke="#2e9a3a" stroke-width="2.5"/></svg>Praesent id arcu slue, malesuada velit faucibus metus.</li>
      <li><svg width="14" height="12"><path d="M1 6l4 4 8-9" fill="none" stroke="#2e9a3a" stroke-width="2.5"/></svg>Donec dolor lacus, tempor eu enim id, porta sagittis nunc.</li>
      <li><svg width="14" height="12"><path d="M1 6l4 4 8-9" fill="none" stroke="#2e9a3a" stroke-width="2.5"/></svg>Aliquam erat volutpabitur tortor justo,</li>
    </ul>
    <div class="pill">Get This Plan →</div>
  </div>
</section>

<section class="portfolio">
  <div class="abs title-wrap"><span class="script">Our</span><span class="heading">Portfolio</span></div>

  <div class="abs work" style="left:48px;top:255px">
    <div class="frame">
      <svg class="ring-svg" width="260" height="260" viewBox="0 0 260 260" aria-hidden="true"><path d="M130 8 A120 120 0 0 1 250 128 L226 128 A96 96 0 0 0 130 32 Z" fill="#3a9bb3"/></svg>
      <div class="photo" style="background:radial-gradient(circle at 50% 50%,#d8d3cc 0,#9fa4ad 55%,#5d6472 100%)" role="img" aria-label="Photo of a team meeting around a table"></div>
    </div>
    <h3>SEO Busines</h3><p>Risus cmodo viverra maecenas<br>accumsan lacus vel facilisis.</p>
  </div>

  <div class="abs work" style="left:418px;top:255px">
    <div class="frame">
      <svg class="ring-svg" width="260" height="260" viewBox="0 0 260 260" aria-hidden="true"><path d="M130 8 A120 120 0 0 1 250 128 L226 128 A96 96 0 0 0 130 32 Z" fill="#3a9bb3"/></svg>
      <div class="photo" style="background:radial-gradient(circle at 50% 45%,#f1e6d8 0,#cfd6de 55%,#8e9bab 100%)" role="img" aria-label="Photo of a woman presenting marketing materials"></div>
    </div>
    <h3>Marketing</h3><p>Risus cmodo viverra maecenas<br>accumsan lacus vel facilisis.</p>
  </div>

  <div class="abs work" style="left:785px;top:255px">
    <div class="frame">
      <svg class="ring-svg" width="260" height="260" viewBox="0 0 260 260" aria-hidden="true"><path d="M130 8 A120 120 0 0 1 250 128 L226 128 A96 96 0 0 0 130 32 Z" fill="#3a9bb3"/></svg>
      <div class="photo" style="background:radial-gradient(circle at 55% 45%,#c9684e 0,#8a5a50 40%,#e6e4e0 100%)" role="img" aria-label="Photo of a presenter at a whiteboard"></div>
    </div>
    <h3>SEO Busines</h3><p>Risus cmodo viverra maecenas<br>accumsan lacus vel facilisis.</p>
  </div>
</section>

<section class="testimonials">
  <div class="abs title-wrap"><span class="script">Client</span><span class="heading">Testimonials</span></div>
  <div class="abs quote" style="left:168px;top:284px;width:270px;height:270px">
    <div class="mark">“</div><p>Lorem ipsum doet, consectetur<br>adipiscing elit. Proin ut turpis ac<br>diam tincidunt auctor sit amet<br>aliquet justo.</p><b>Alex Carter</b><em>Simply Dummy</em>
  </div>
  <div class="abs quote" style="left:746px;top:284px;width:270px;height:270px">
    <div class="mark">“</div><p>Lorem ipsum doet, consectetur<br>adipiscing elit. Proin ut turpis ac<br>diam tincidunt auctor sit amet<br>aliquet justo.</p><b>Alex Carter</b><em>Simply Dummy</em>
  </div>
  <div class="abs quote main" style="left:432px;top:242px;width:320px;height:320px">
    <div class="mark">“</div><p>Lorem ipsum doet, consectetur<br>adipiscing elit. Proin ut turpis ac<br>diam tincidunt auctor sit amet<br>aliquet justo. In ac dui imperdiet<br>nibh posuereusa.</p><b>Alex Carter</b><em>Simply Dummy</em>
  </div>
</section>

<section class="contact">
  <svg class="abs" style="left:660px;top:40px" width="520" height="560" viewBox="0 0 520 560" aria-hidden="true">
    <path d="M30 250 C60 120 200 30 360 40 C440 45 500 80 510 110" fill="none" stroke="#2fb0cb" stroke-width="16" stroke-linecap="round" opacity=".8"/>
    <path d="M50 280 C90 150 220 70 380 70" fill="none" stroke="#7fd3e2" stroke-width="5" stroke-linecap="round" opacity=".8"/>
    <path d="M500 400 C490 460 470 500 440 530" fill="none" stroke="#2fb0cb" stroke-width="8" stroke-linecap="round" opacity=".7"/>
  </svg>
  <div class="abs figure" role="img" aria-label="Photo of a smiling man in a suit holding a laptop and pointing to it"></div>
  <div class="abs script">Get in Touch</div>
  <h2 class="abs heading">Leave Us A Message</h2>
  <div class="abs field" style="left:85px;top:283px;width:282px">First Name</div>
  <div class="abs field" style="left:376px;top:283px;width:282px">Last Name</div>
  <div class="abs field" style="left:85px;top:335px;width:282px">Email</div>
  <div class="abs field" style="left:376px;top:335px;width:282px">Phone</div>
  <div class="abs field" style="left:85px;top:388px;width:573px;height:124px">Message</div>
  <div class="abs pill btn-teal">Submit Message →</div>
</section>

<footer class="footer">
  <div class="abs" style="left:85px;top:108px;width:300px">
    <h4>ABOUT US</h4>
    <p style="margin-top:12px">Lorem ipsum doloamet, consectetur adipiscing elit, sed do eiusmod tempor incididunt ut labore et dolore maa aliqua. Quis ipsum suspendisse ultrices gravida</p>
    <div class="chips" style="margin-top:10px"><span>Pingo</span><span>Wavelet</span><span>Guildhall</span></div>
  </div>
  <div class="abs" style="left:445px;top:108px">
    <h4>QUICK LINKS</h4>
    <ul style="margin-top:12px;line-height:36px"><li>Home</li><li>About</li><li>Services</li><li>Portfolio</li><li>Contact</li></ul>
  </div>
  <div class="abs" style="left:632px;top:108px;width:240px">
    <h4>CONTAC US</h4>
    <div class="contact-row" style="margin-top:12px"><svg width="12" height="14"><path d="M6 0a5 5 0 0 0-5 5c0 4 5 9 5 9s5-5 5-9a5 5 0 0 0-5-5z" fill="#2fb0cb"/><circle cx="6" cy="5" r="2" fill="#1d1e22"/></svg><span>14 Harbor Lane, Portland,<br>ME 04101, United States</span></div>
    <div class="contact-row" style="margin-top:8px"><svg width="14" height="10"><rect width="14" height="10" rx="1" fill="#2fb0cb"/><path d="M0 1l7 5 7-5" fill="none" stroke="#1d1e22" stroke-width="1.2"/></svg><span>hello@brookoutreach.example</span></div>
    <div class="contact-row" style="margin-top:8px"><svg width="14" height="14"><path d="M3 0l3 3-2 2c1 2 3 4 5 5l2-2 3 3-2 3C6 14 0 8 0 3z" fill="#2fb0cb"/></svg><span>1800-555-019</span></div>
  </div>
  <div class="abs brand" style="left:900px;top:160px;font-size:22px"><i></i>Brook Outreach</div>
  <div class="abs payments"><span>Payline</span><span>Orbit</span><span>Nova</span><span>SendWise</span></div>
  <div class="abs rule"></div>
  <div class="abs copy">© 2023 <span>Brook Outreach</span> . All right reserved</div>
</footer>

</body>
</html>
```